Custom Real Estate Postcard for Buying Communities

We are a real estate company that owns/operates mobile home parks and want to send out a postcard to owners of these communities letting them know who our company is and let them know we want to buy their community. We are looking to create a postcard that introduces our company to the owner and also lets them know we want to buy their community - we are targeting older mom & pop type communities so we would like the postcard to have a home-y feel that makes the owner feel like our company will treat them fairly during the acquisition process
I have attached a few images from our communities that might look good on a postcard - you don't need to use all of them, I just included multiple so there are different options. please feel free to edit/enhance the images if needed.
Our company is Brightfield Residential Partners (BRP) and the logo is attached.
Text to be included somewhere on postcard: "We pride ourselves on active hands-on management in order to provide our residents quality communities at an affordable price.
BRP is a proven owner/operator and has the ability to purchase without any financing contingencies.
We provide a quick and easy closing. We do not retrade
Target Market(s)
Owners of Mobile Home Parks that BRP (our company) would like to acquire - small mom & pop owners that want to see that we aren't the big firm trying to come in and take over but a local company that will still treat the residents well
Industry/Entity Type
Real Estate
Colors
Designer to choose colors to be used in the design.
Requirements
Must have
- The BRP logo, at least one picture of a mobile home park from the attached pictures. And some version/form of the provided text. Info/contact section with website (www.brphomesites.com), email (info@brphomesites.com) and phone (555.284.7096)
- Something sort of call to action like: "We Want to Buy Your Community", "Ready to Sell?", "Interested in Selling?" etc.
Nice to have
- BRP Logo Colors, in addition to any other colors if designer thinks there are complimentary colors

```html
<!DOCTYPE html>
<html lang="en">
<head>
<meta charset="utf-8">
<title>Brightfield Residential Partners – Postcard</title>
<link href="https://fonts.googleapis.com/css2?family=Open+Sans:wght@300;400;600;800&family=Oswald:wght@300;500&display=swap" rel="stylesheet">
<style>
  :root{
    --page:#e4e4e4;
    --panel:#eeeeee;
    --white:#ffffff;
    --brown:#7a3220;
    --brown-dark:#5e2416;
    --gold:#b48a3c;
    --gold-light:#e9c27a;
    --ink:#262626;
    --soft-ink:#3a3a3a;
  }
  *{margin:0;padding:0;box-sizing:border-box}
  html,body{width:960px;height:1200px;overflow:hidden;background:var(--page)}
  body{position:relative;font-family:"Open Sans",sans-serif;color:var(--ink)}
  .card{position:absolute;left:125px;width:713px;height:461px;background:var(--white);overflow:hidden}
  .card--front{top:98px;background:var(--panel)}
  .card--back{top:658px}
  .card-art{position:absolute;inset:0;width:100%;height:100%}
  .brand{position:absolute;display:flex;align-items:center;gap:14px}
  .brand-dot{width:16px;height:16px;border-radius:50%;background:var(--brown);flex:none}
  .brand-name{font-family:"Open Sans",sans-serif;font-weight:400;color:var(--ink);letter-spacing:2px;line-height:1.08;text-transform:uppercase}
  .card--front .brand{left:32px;top:36px}
  .card--front .brand-name{font-size:24px}
  .intro{position:absolute;left:0;top:154px;width:360px;height:159px;padding:10px 0 0 17px;color:var(--white)}
  .intro-title{font-family:"Oswald",sans-serif;font-weight:500;font-size:21px;letter-spacing:.3px;line-height:1.2;text-transform:uppercase}
  .intro-tags{font-family:"Oswald",sans-serif;font-weight:300;font-size:18px;letter-spacing:.8px;line-height:1.2;margin-bottom:10px}
  .intro-copy{font-size:10.4px;line-height:1.42;width:318px}
  .intro-copy p+p{margin-top:4px}
  .headline{position:absolute;left:30px;top:340px;font-weight:800;font-size:35px;letter-spacing:.5px;color:var(--ink)}
  .contact-bar{position:absolute;left:0;bottom:0;width:100%;height:51px;background:linear-gradient(90deg,var(--gold) 0%,var(--gold-light) 38%,var(--gold) 70%,#c9a05a 100%);display:flex;align-items:center;color:var(--white);font-size:14.5px}
  .call-pill{margin-left:27px;width:221px;height:28px;border-radius:14px;background:linear-gradient(#f2f2f2,#cfcfcf);color:var(--soft-ink);font-size:15px;display:flex;align-items:center;justify-content:center}
  .contact-item{display:flex;align-items:center;gap:8px}
  .contact-item svg{width:13px;height:13px;flex:none}
  .contact-bar .mail{margin-left:54px}
  .contact-bar .divider{width:1px;height:32px;background:rgba(255,255,255,.7);margin:0 30px 0 34px}
  .card--back .brand{left:74px;top:20px;gap:10px}
  .card--back .brand-name{font-size:17px;letter-spacing:1.6px}
  .card--back .brand-dot{width:13px;height:13px}
  .ribbon-top{position:absolute;left:86px;top:238px;width:207px;height:21px;background:var(--brown);color:var(--white);font-size:11.5px;display:flex;align-items:center;justify-content:center}
  .ribbon-main{position:absolute;left:48px;top:259px;width:283px;height:27px;background:var(--gold);color:var(--white);font-size:13px;font-weight:600;letter-spacing:.3px;display:flex;align-items:center;justify-content:center;box-shadow:0 6px 8px -6px rgba(0,0,0,.45)}
  .promise{position:absolute;left:48px;top:300px;width:283px;text-align:center;color:var(--brown);font-weight:600;font-size:13px;line-height:1.3}
  .back-contacts{position:absolute;left:22px;top:343px;font-size:11px;line-height:1.45;color:var(--ink)}
  .back-contacts .contact-item{gap:7px}
  .back-contacts .phone{font-size:14px;font-weight:600;margin-bottom:1px}
  .back-contacts svg{width:11px;height:11px}
  .back-contacts .phone svg{width:14px;height:14px}
  .cta{position:absolute;left:211px;top:346px;text-transform:uppercase;color:var(--brown);line-height:1}
  .cta-small{display:block;font-weight:300;font-size:21px;letter-spacing:.5px}
  .cta-big{display:block;font-weight:800;font-size:27px}
  .stamp-box{position:absolute;left:601px;top:28px;width:83px;height:83px;border:1px solid #9a9a9a}
  .address-line{position:absolute;left:471px;width:213px;height:1px;background:#555}
</style>
</head>
<body>

<section class="card card--front">
  <svg class="card-art" viewBox="0 0 713 461" preserveAspectRatio="none">
    <defs>
      <linearGradient id="front-photo" x1="0" y1="0" x2="0" y2="1">
        <stop offset="0" stop-color="#2f7fc8"/>
        <stop offset=".28" stop-color="#5f8f4a"/>
        <stop offset=".55" stop-color="#c9cbc6"/>
        <stop offset=".75" stop-color="#6f9a3c"/>
        <stop offset="1" stop-color="#8aa64c"/>
      </linearGradient>
      <linearGradient id="band" x1="0" y1="0" x2="1" y2="0">
        <stop offset="0" stop-color="#7a3220"/>
        <stop offset="1" stop-color="#8c3d24"/>
      </linearGradient>
    </defs>
    <rect x="0" y="154" width="380" height="159" fill="url(#band)"/>
    <path d="M420 0 H439 C330 110 318 320 460 410 H440 C298 320 312 110 420 0 Z" fill="var(--white)"/>
    <path d="M430 0 H447 C338 110 326 318 468 410 H455 C306 320 318 110 430 0 Z" fill="var(--brown)"/>
    <path d="M447 0 H713 V410 H468 C326 318 338 110 447 0 Z" fill="url(#front-photo)" role="img" aria-label="Photo of a white manufactured home with green trim, flowering shrubs and lawn under tall pines"/>
  </svg>

  <div class="brand">
    <span class="brand-dot"></span>
    <div class="brand-name">Brightfield<br>Residential<br>Partners</div>
  </div>

  <div class="intro">
    <h1 class="intro-title">Brightfield Residential Partners</h1>
    <div class="intro-tags">LOCAL &nbsp;•&nbsp; EXPERIENCED &nbsp;•&nbsp; TRUSTED</div>
    <div class="intro-copy">
      <p>We pride ourselves on active hands-on management in order to provide our residents quality communities at an affordable price.</p>
      <p>BRP is a proven owner/operator and has the ability to purchase without any financing contingencies.</p>
    </div>
  </div>

  <h2 class="headline">READY TO SELL?</h2>

  <div class="contact-bar">
    <div class="call-pill">Call Us: +1 555 284 7096</div>
    <div class="contact-item mail">
      <svg viewBox="0 0 16 16"><circle cx="8" cy="8" r="8" fill="#222"/><rect x="3.5" y="5" width="9" height="6" fill="none" stroke="#fff" stroke-width="1.2"/><path d="M3.5 5 L8 8.6 L12.5 5" fill="none" stroke="#fff" stroke-width="1.2"/></svg>
      <span>info@brphomesites.com</span>
    </div>
    <span class="divider"></span>
    <div class="contact-item web">
      <svg viewBox="0 0 16 16"><circle cx="8" cy="8" r="8" fill="#222"/><circle cx="8" cy="8" r="4.6" fill="none" stroke="#fff" stroke-width="1"/><ellipse cx="8" cy="8" rx="2" ry="4.6" fill="none" stroke="#fff" stroke-width="1"/><path d="M3.4 8 H12.6" stroke="#fff" stroke-width="1"/></svg>
      <span>www.brphomesites.com</span>
    </div>
  </div>
</section>

<section class="card card--back">
  <svg class="card-art" viewBox="0 0 713 461" preserveAspectRatio="none">
    <defs>
      <linearGradient id="aerial" x1="0" y1="0" x2="1" y2="1">
        <stop offset="0" stop-color="#3f6b2c"/>
        <stop offset=".5" stop-color="#7e9a6a"/>
        <stop offset="1" stop-color="#a9b3a4"/>
      </linearGradient>
      <clipPath id="panel-shape"><path d="M0 0 H327 C420 120 420 280 319 396 H0 Z"/></clipPath>
    </defs>
    <path d="M0 0 H327 C420 120 420 280 319 396 H0 Z" fill="var(--panel)"/>
    <rect x="0" y="94" width="420" height="140" fill="url(#aerial)" clip-path="url(#panel-shape)" role="img" aria-label="Aerial photo of a manufactured home community with tree-lined streets"/>
    <path d="M327 0 H342 C438 125 432 290 319 396 C412 280 420 120 327 0 Z" fill="#6b4a1e"/>
  </svg>

  <div class="brand">
    <span class="brand-dot"></span>
    <div class="brand-name">Brightfield<br>Residential<br>Partners</div>
  </div>

  <div class="ribbon-top">Interested In Selling?</div>
  <div class="ribbon-main">We want to buy your community</div>

  <p class="promise">We provide a quick &amp; easy closing<br>We do not retrade</p>

  <div class="back-contacts">
    <div class="contact-item phone">
      <svg viewBox="0 0 16 16"><circle cx="8" cy="8" r="8" fill="var(--brown)"/><path d="M5.2 4 L6.8 4 L7.4 6.2 L6.4 7 C6.9 8.2 7.8 9.1 9 9.6 L9.8 8.6 L12 9.2 L12 10.8 C12 11.4 11.5 11.8 10.9 11.8 C7.3 11.5 4.5 8.7 4.2 5.1 C4.2 4.5 4.6 4 5.2 4 Z" fill="#fff"/></svg>
      <span>+1 555 284 7096</span>
    </div>
    <div class="contact-item">
      <svg viewBox="0 0 16 16"><rect x="1" y="3.5" width="14" height="9" fill="var(--brown)"/><path d="M1 3.5 L8 9 L15 3.5" fill="none" stroke="#fff" stroke-width="1.2"/></svg>
      <span>info@brphomesites.com</span>
    </div>
    <div class="contact-item">
      <svg viewBox="0 0 16 16"><circle cx="8" cy="8" r="7" fill="var(--brown)"/><ellipse cx="8" cy="8" rx="2.6" ry="6" fill="none" stroke="#fff" stroke-width="1"/><path d="M2 8 H14" stroke="#fff" stroke-width="1"/></svg>
      <span>www.brphomesites.com</span>
    </div>
  </div>

  <div class="cta">
    <span class="cta-small">Call Us</span>
    <span class="cta-big">Today</span>
  </div>

  <div class="stamp-box"></div>
  <span class="address-line" style="top:194px"></span>
  <span class="address-line" style="top:231px"></span>
  <span class="address-line" style="top:270px"></span>
  <span class="address-line" style="top:308px"></span>
</section>

</body>
</html>
```